Quorvane Capital Modern Business Card

We need a modern business card template designed for Quorvane Capital.
Quorvane Capital is a diversified global cryptocurrency investment fund.

The font under the logo: Hiragino Kaku Gothic Pro

Color Hexcode: Main colors white (ffffff) & teal (188383), we are open to adding #fcca46 as an accent

Target Market(s)

Accredited Investors, high net worth individuals and institutional investors

Industry/Entity Type

Investment

Contact Information for Business Card

Contact Information should contain
Name
main phone +1 720 555 0147
cell
email

Font styles to use
Sans Serif
Other font styles liked:
• Hiragino Kaku Gothic Pro

Requirements
Must have
• would like to have icons that identify the contact information
• include our website: www.quorvanecapital.example
• include our Tagline: Diversified Crypto Investment Funds
Nice to have
• Would like to have a simple back side with the logo (without the words) and plenty of space

```html
<!DOCTYPE html>
<html lang="en">
<head>
<meta charset="utf-8">
<title>Quorvane Capital — Business Card</title>
<link href="https://fonts.googleapis.com/css2?family=Roboto:wght@300;400;500&display=swap" rel="stylesheet">
<style>
  :root {
    --stage: #2f2f2f;
    --paper: #ffffff;
    --teal: #188383;
    --accent: #fcca46;
    --ink: #1c1c1c;
    --icon: #2a9a9a;
  }
  * { box-sizing: border-box; margin: 0; padding: 0; }
  html, body {
    width: 1200px; height: 880px; overflow: hidden;
    background: var(--stage);
    font-family: "Roboto", Arial, sans-serif;
  }
  .stage {
    width: 1200px; height: 880px;
    display: flex; flex-direction: column;
    align-items: center; justify-content: center; gap: 40px;
  }
  .card {
    position: relative;
    width: 672px; height: 384px;
    background: var(--paper);
    overflow: hidden;
    box-shadow: 0 10px 30px rgba(0,0,0,.45);
  }

  /* Back side */
  .card--back .wordmark {
    position: absolute; left: 0; right: 0; top: 168px;
    text-align: center;
    font-size: 34px; font-weight: 400; letter-spacing: 1px;
    color: var(--teal); text-transform: uppercase;
  }

  /* Front side */
  .accent-panel { position: absolute; inset: 0; }
  .card--front .wordmark {
    position: absolute; left: 40px; top: 280px;
    font-size: 24px; font-weight: 400; letter-spacing: .5px;
    color: var(--ink); text-transform: uppercase;
  }
  .holder {
    position: absolute; left: 318px; top: 42px;
    color: var(--teal);
  }
  .holder__name {
    font-size: 27px; font-weight: 400; text-transform: uppercase; letter-spacing: .3px;
  }
  .holder__role { font-size: 15px; text-transform: uppercase; margin-top: 2px; }
  .contacts {
    position: absolute; left: 318px; top: 126px;
    list-style: none;
    font-size: 15px; color: var(--ink);
  }
  .contacts li {
    display: flex; align-items: center; gap: 12px;
    height: 27px;
  }
  .contacts svg { width: 16px; height: 16px; flex: none; }
  .tagline {
    position: absolute; right: 28px; bottom: 40px;
    font-size: 21px; font-weight: 400; color: var(--ink);
  }
</style>
</head>
<body>
<main class="stage">

  <section class="card card--back" aria-label="Card back">
    <p class="wordmark">Quorvane Capital</p>
  </section>

  <section class="card card--front" aria-label="Card front">
    <svg class="accent-panel" viewBox="0 0 672 384" aria-hidden="true">
      <polygon points="0,384 0,196 210,150 400,232 360,384" fill="var(--accent)"/>
    </svg>
    <p class="wordmark">Quorvane Capital</p>

    <div class="holder">
      <p class="holder__name">Maren Castell</p>
      <p class="holder__role">CEO</p>
    </div>

    <ul class="contacts">
      <li>
        <svg viewBox="0 0 16 16" aria-hidden="true"><rect x="4" y="1" width="8" height="14" rx="1.5" fill="none" stroke="var(--icon)" stroke-width="1.4"/><circle cx="8" cy="12.5" r=".9" fill="var(--icon)"/></svg>
        <span>+1 720 555 0162</span>
      </li>
      <li>
        <svg viewBox="0 0 16 16" aria-hidden="true"><path d="M4 1.5l2.3 3-1.4 1.6c.8 2 2.4 3.6 4.4 4.4l1.6-1.4 3 2.3-1.5 2.6C7.6 13.6 2.4 8.4 1.4 3z" fill="var(--icon)"/></svg>
        <span>+1 720 555 0147</span>
      </li>
      <li>
        <svg viewBox="0 0 16 16" aria-hidden="true"><rect x="1.5" y="3.5" width="13" height="9" fill="none" stroke="var(--icon)" stroke-width="1.4"/><path d="M1.5 3.5L8 9l6.5-5.5" fill="none" stroke="var(--icon)" stroke-width="1.4"/></svg>
        <span>hello@quorvanecapital.example</span>
      </li>
      <li>
        <svg viewBox="0 0 16 16" aria-hidden="true"><circle cx="8" cy="8" r="6.5" fill="none" stroke="var(--icon)" stroke-width="1.4"/><ellipse cx="8" cy="8" rx="2.8" ry="6.5" fill="none" stroke="var(--icon)" stroke-width="1.2"/><path d="M1.5 8h13" stroke="var(--icon)" stroke-width="1.2"/></svg>
        <span>www.quorvanecapital.example</span>
      </li>
    </ul>

    <p class="tagline">Diversified Crypto Investment Funds</p>
  </section>

</main>
</body>
</html>
```